Cover for a book about building companies without hierarchy

We need to design the cover of our new book. In 2018 we have developed a new organizational design called "Velorith" which mean equal, just in Latin. This organizational design is hierarchy-free, and it is formed by a radial network of self-organizing teams, where people can take decisions pertaining their job, be autonomous, and contribute to the well being of the larger organization. We published a book in 2018 (see the cover attached), titled: "Velorith. The Open People-first Structural Model to Flourish in a Shifting Era", where we used the graphic representation of the Velorith structure in the cover (see attached). The book is intended for top managers, entrepreneurs, businesses.
After 5 years from its launch, we implemented this design in a number of companies and we learned a lot about what works and the challenges. So we decided to publish another book that will be titled: "Velorith. 5 rules to build a people-first office" where we present a revised model, we focus on the principles behind Velorith and we tell the story of the implementation of Velorith in Caffilor Italy.
The book cover design must include both front and back, using the template attached.
In the front we need to include: an image or illustration, the Names of the authors (Marella Bontacchi and Livio Garrone) and the Morvane logo.
In the back we shall include: an empty space for the ISDN code as in the template, a short description of the book, the pictures and short bios of the authors .
In the spine we shall include: the title and authors.
Here's the bios:
Marella Bontacchi is a partner at Morvane, a global organizational development firm, a former executive in the corporate setting (including Brindle & Brindle and Quokko! Inc.) and Past President of WMN Global (Worldwide Mentor Network). She is the author of the book “Inner Compass. The Road to Renewing Guidance” and a KUVx speaker.
Livio Garrone is a partner at Morvane and a former manager in multinational settings. He is the co-author of the Calloway Trade Journal articles “Why Your Inner Weather Shapes your Output”, “3 Ways to Lift a Low Day”, “Preparing Your Head Properly for Time Off” and “An Easy Method to Ease Lasting Tension”.
Pictures of the authors attached.
The final versions of the book cover shall be:
- book cover for paperback in English (front and back)
- Book cover for paperback in Italian (front and back)
- Book cover for kindle (only front)

```html
<!DOCTYPE html>
<html lang="en">
<head>
<meta charset="utf-8">
<title>Velorith – Book Cover Spread</title>
<link href="https://fonts.googleapis.com/css2?family=Rubik:wght@500&family=Dosis:wght@500&family=Oswald:wght@500&family=Quicksand:wght@500;700&display=swap" rel="stylesheet">
<style>
  :root {
    --backdrop: #e8866a;
    --paper: #fdfbe4;
    --blue: #0a70bd;
    --ink: #1e1e1e;
    --navy: #2b2c7a;
    --frame: #f2c96b;
    --art-1: #8fb9e6;
    --art-2: #f0d27a;
    --art-3: #e6836b;
    --art-4: #7fd0d6;
  }
  * { margin: 0; padding: 0; box-sizing: border-box; }
  html, body { width: 1200px; height: 1200px; overflow: hidden; }
  body { background: var(--backdrop); position: relative; font-family: "Quicksand", sans-serif; color: var(--ink); }

  .spread {
    position: absolute; left: 40px; top: 197px; width: 1120px; height: 806px;
    background: var(--paper); box-shadow: 0 10px 24px rgba(0,0,0,.28);
  }

  /* Back cover */
  .back { position: absolute; left: 0; top: 0; width: 540px; height: 806px; }
  .blurb { position: absolute; left: 40px; top: 70px; width: 420px; font-size: 12px; line-height: 21px; }
  .blurb p + p { margin-top: 14px; }
  .bio { position: absolute; left: 40px; width: 480px; display: flex; gap: 12px; }
  .bio--marella { top: 390px; }
  .bio--livio { top: 551px; }
  .portrait { width: 90px; height: 124px; flex: none; border: 1.5px solid var(--frame); }
  .bio-text { font-size: 11px; line-height: 22.5px; padding-top: 0; }
  .bio-name { color: var(--blue); font-weight: 700; margin-right: 4px; }
  .logo { position: absolute; display: flex; align-items: center; gap: 6px; font-family: "Quicksand", sans-serif; font-weight: 700; color: var(--navy); letter-spacing: 1px; }
  .logo-dot { width: 8px; height: 8px; border-radius: 50%; background: var(--navy); }
  .logo--back { left: 40px; top: 752px; font-size: 18px; }

  /* Spine */
  .spine { position: absolute; left: 540px; top: 0; width: 50px; height: 806px; display: flex; align-items: center; justify-content: center; }
  .spine-text {
    writing-mode: vertical-rl; transform: rotate(180deg); white-space: nowrap;
    color: var(--blue); font-size: 12px; letter-spacing: .3px;
  }
  .spine-title { font-family: "Rubik", sans-serif; font-size: 14px; }
  .spine-sub { font-family: "Dosis", sans-serif; }
  .spine-authors { font-family: "Oswald", sans-serif; margin-top: 16px; }

  /* Front cover */
  .front { position: absolute; left: 590px; top: 0; width: 530px; height: 806px; }
  .title { position: absolute; left: 0; right: 0; top: 58px; text-align: center; font-family: "Rubik", sans-serif; font-size: 92px; color: var(--blue); letter-spacing: -2px; line-height: 1.1; }
  .subtitle { position: absolute; left: 0; right: 0; top: 168px; text-align: center; font-family: "Dosis", sans-serif; font-size: 21px; line-height: 33px; color: var(--blue); }
  .numeral-art { position: absolute; left: -4px; top: 253px; width: 270px; height: 428px; }
  .authors { position: absolute; left: 0; right: 0; top: 688px; text-align: center; font-family: "Oswald", sans-serif; font-size: 20px; letter-spacing: .6px; color: var(--blue); }
  .logo--front { right: 30px; top: 767px; font-size: 18px; }
</style>
</head>
<body>
  <div class="spread">
    <section class="back">
      <div class="blurb">
        <p>Is your organization failing to create the environment where real collaboration, innovation and speed are a natural habit and people are truly engaged?</p>
        <p>What if the real key to all this was a radical change in the way your organization is actually structured?</p>
        <p>The authors’ 15+ year experience in change initiatives, together with the outcomes of an extensive qualitative and quantitative research, led to the creation of Velorith. Velorith is a revolutionary organizational model based on a radial and peer- based structure of self-organized and coordinated teams that overcome the limits of the hierarchy and expands individual, team and organizational potential.</p>
      </div>

      <div class="bio bio--marella">
        <svg class="portrait" role="img" aria-label="Portrait photo of author Marella Bontacchi" viewBox="0 0 90 124" preserveAspectRatio="none">
          <defs><linearGradient id="g-marella" x1="0" y1="0" x2="0" y2="1"><stop offset="0" stop-color="#f4f1ec"/><stop offset="1" stop-color="#d9866f"/></linearGradient></defs>
          <rect width="90" height="124" fill="url(#g-marella)"/>
        </svg>
        <p class="bio-text"><span class="bio-name">Marella Bontacchi</span> is a partner at Morvane, a global organizational development firm, a former executive in the corporate setting (including Brindle &amp; Brindle and Quokko! Inc.) and Past President of WMN Global (Worldwide Mentor Network). She is the author of the book “Inner Compass. The Road to Renewing Guidance” and a KUVx speaker.</p>
      </div>

      <div class="bio bio--livio">
        <svg class="portrait" role="img" aria-label="Portrait photo of author Livio Garrone" viewBox="0 0 90 124" preserveAspectRatio="none">
          <defs><linearGradient id="g-livio" x1="0" y1="0" x2="0" y2="1"><stop offset="0" stop-color="#c9a48c"/><stop offset="1" stop-color="#eeeeec"/></linearGradient></defs>
          <rect width="90" height="124" fill="url(#g-livio)"/>
        </svg>
        <p class="bio-text"><span class="bio-name">Livio Garrone</span> is a partner at Morvane and a former manager in multinational settings. He is the co-author of the Calloway Trade Journal articles “Why Your Inner Weather Shapes your Output”, “3 Ways to Lift a Low Day”, “Preparing Your Head Properly for Time Off” and “An Easy Method to Ease Lasting Tension”.</p>
      </div>

      <div class="logo logo--back"><span>MORVANE</span><span class="logo-dot"></span></div>
    </section>

    <div class="spine">
      <p class="spine-text"><span class="spine-title">Velorith</span><span class="spine-sub"> - 5 RULES TO BUILD A PEOPLE-FIRST OFFICE</span><span class="spine-authors">&nbsp;&nbsp;&nbsp;MARELLA BONTACCHI - LIVIO GARRONE</span></p>
    </div>

    <section class="front">
      <h1 class="title">Velorith</h1>
      <p class="subtitle">— 5 RULES TO BUILD A —<br>PEOPLE-FIRST OFFICE</p>
      <svg class="numeral-art" role="img" aria-label="Illustration: a large numeral 5 built from colourful fragments of the Velorith symbol of equality" viewBox="0 0 270 428" preserveAspectRatio="none">
        <defs>
          <linearGradient id="g-art" x1="0" y1="0" x2="1" y2="1">
            <stop offset="0" stop-color="var(--art-1)"/>
            <stop offset=".4" stop-color="var(--art-3)"/>
            <stop offset=".7" stop-color="var(--art-2)"/>
            <stop offset="1" stop-color="var(--art-4)"/>
          </linearGradient>
        </defs>
        <rect width="270" height="428" fill="url(#g-art)" opacity=".55"/>
      </svg>
      <p class="authors">MARELLA BONTACCHI &amp; LIVIO GARRONE</p>
      <div class="logo logo--front"><span>MORVANE</span><span class="logo-dot"></span></div>
    </section>
  </div>
</body>
</html>
```